Anchorwell Giving - New Website Designed

I need a site that looks like this http://www.lumenhavenfund.org for boat donations. So please replace the cars with boats.

```html
<!DOCTYPE html>
<html lang="en">
<head>
<meta charset="utf-8">
<title>Anchorwell Giving – Donate Your Boat</title>
<link rel="stylesheet" href="https://fonts.googleapis.com/css2?family=Roboto+Condensed:wght@400;700&family=Mulish:wght@400;600;700&display=swap">
<style>
:root{
  --navy:#12287a;
  --navy-deep:#0b1a4f;
  --red:#fe2d3f;
  --cream:#f4efe8;
  --ink:#2b2b2b;
  --text:#555;
  --dark:#303030;
  --footer:#1b1b1f;
  --white:#fff;
}
*{box-sizing:border-box;margin:0;padding:0}
html,body{width:1200px;height:2344px;overflow:hidden}
body{position:relative;background:var(--white);font-family:'Mulish',sans-serif;color:var(--ink)}
.abs{position:absolute}
.condensed{font-family:'Roboto Condensed',sans-serif}

/* header + hero */
.hero-bg{left:0;top:0;width:1200px;height:564px;background:linear-gradient(100deg,#0c1530 0%,#2a2f4a 35%,#4a2330 60%,#2a1d2c 100%)}
.soldier-photo{left:78px;top:250px;width:347px;height:314px;background:radial-gradient(ellipse at 50% 55%,#7d6b52 0%,#5a4d3c 50%,rgba(40,40,50,0) 85%)}
.brand{left:89px;top:28px;display:flex;align-items:center;gap:16px;color:var(--white)}
.brand-mark{width:56px;height:56px;border-radius:50%;background:var(--white)}
.brand-name{font-family:'Roboto Condensed',sans-serif;font-size:34px;line-height:36px;font-weight:400;text-transform:uppercase}
.nav{left:0;top:131px;width:1200px;height:58px;background:var(--navy)}
.nav a{position:absolute;top:20px;color:var(--white);font-size:15px;font-weight:600;text-decoration:none;text-transform:uppercase}
.hero-title{left:340px;top:308px;width:372px;text-align:right;color:var(--white);font-family:'Roboto Condensed',sans-serif;font-weight:700;font-size:54px;line-height:62px}

/* donation panel */
.donate-panel{left:736px;top:0;width:378px;height:564px;background:var(--red);color:var(--white)}
.call{position:absolute;left:0;top:0;width:378px;height:131px;border-bottom:1px solid rgba(255,255,255,.35)}
.call-icon{position:absolute;left:32px;top:39px;width:53px;height:53px;border-radius:50%;background:var(--white)}
.call-icon svg{position:absolute;left:14px;top:14px}
.call-label{position:absolute;left:106px;top:42px;font-size:19px;font-weight:600;text-transform:uppercase}
.call-number{position:absolute;left:106px;top:66px;font-size:28px;font-weight:700}
.panel-title{position:absolute;left:0;top:141px;width:378px;text-align:center;font-size:23px;font-weight:700;text-transform:uppercase}
.panel-divider{position:absolute;left:0;top:186px;width:378px;height:1px;background:rgba(255,255,255,.35)}
.group-label{position:absolute;left:11px;font-size:17px;font-weight:400}
.field{position:absolute;height:30px;background:var(--white);color:#666;font-size:12px;line-height:30px;padding-left:12px}
.field .caret{position:absolute;right:12px;top:13px;width:0;height:0;border-left:5px solid transparent;border-right:5px solid transparent;border-top:5px solid #555}
.submit{position:absolute;left:11px;top:464px;width:356px;height:55px;background:var(--navy);border-radius:3px;text-align:center;line-height:55px;font-size:19px;font-weight:600;text-transform:uppercase}

/* benefits */
.section-heading{left:0;width:1200px;text-align:center;font-family:'Roboto Condensed',sans-serif;font-size:30px;font-weight:400;color:var(--ink);text-transform:uppercase}
.benefit{top:709px;width:190px;text-align:center}
.benefit-icon{width:94px;height:94px;border-radius:50%;background:var(--navy);margin:0 auto;display:flex;align-items:center;justify-content:center}
.benefit-icon.accent{background:var(--red)}
.benefit-label{margin-top:30px;font-size:18px;line-height:23px;color:var(--text);font-weight:600}

/* how to donate */
.how{left:0;top:959px;width:1200px;height:391px;background:var(--cream)}
.step{top:1110px;width:320px;text-align:center}
.step-icon{width:102px;height:102px;border-radius:50%;background:var(--navy);margin:0 auto;display:flex;align-items:center;justify-content:center}
.step-label{margin-top:20px;font-size:18px;line-height:24px;color:var(--ink);text-transform:uppercase}

/* faq */
.faq-item{left:88px;width:656px;border-radius:4px;color:var(--white);padding:0 28px}
.faq-item.open{top:1486px;height:158px;background:var(--navy)}
.faq-item.closed{background:var(--dark);height:80px}
.faq-q{font-family:'Roboto Condensed',sans-serif;font-size:18px;line-height:24px}
.faq-item.open .faq-q{margin-top:26px}
.faq-item.closed .faq-q{margin-top:28px}
.faq-a{margin-top:10px;font-size:13px;line-height:21px;color:#d7dcef;width:590px}
.faq-toggle{position:absolute;right:24px;width:16px;height:16px;border:1.5px solid var(--white);border-radius:2px}
.faq-toggle::before{content:"";position:absolute;left:3px;top:6px;width:7px;height:1.5px;background:var(--white)}
.faq-toggle.plus::after{content:"";position:absolute;left:6px;top:3px;width:1.5px;height:7px;background:var(--white)}
.parade-photo{left:767px;top:1486px;width:347px;height:342px;background:linear-gradient(180deg,#6f8a5a 0%,#8d9a86 40%,#7a6d58 70%,#5d5d60 100%)}

/* footer */
.footer-tab{left:488px;top:1917px;width:228px;height:78px}
.footer-tab-brand{left:530px;top:1931px;display:flex;align-items:center;gap:10px;color:var(--white)}
.footer-tab-brand .dot{width:28px;height:28px;border-radius:50%;background:var(--white)}
.footer-tab-brand span{font-family:'Roboto Condensed',sans-serif;font-size:20px;line-height:22px;text-transform:uppercase}
.footer{left:0;top:1995px;width:1200px;height:277px;background:linear-gradient(110deg,#16161a 0%,#24242c 45%,#2c2a2e 70%,#1e1e22 100%)}
.footer-heading{top:2068px;color:var(--white);font-family:'Roboto Condensed',sans-serif;font-size:21px;text-transform:uppercase}
.footer-about{left:86px;top:2111px;width:300px;color:#cfcfcf;font-size:13px;line-height:23.5px}
.sitemap{left:495px;top:2111px;list-style:none;color:#cfcfcf;font-size:13px;line-height:26.5px;text-transform:uppercase}
.sitemap li::before{content:">>";display:inline-block;width:33px}
.newsletter-input{left:792px;top:2117px;width:219px;height:41px;border:1px solid #666;color:#999;font-size:12px;line-height:39px;padding-left:14px}
.newsletter-btn{left:1011px;top:2117px;width:103px;height:41px;background:var(--red);color:var(--white);text-align:center;font-size:16px;line-height:41px;font-weight:600}
.social{top:2181px;width:23px;height:23px;border-radius:50%}
.copyright{left:0;top:2272px;width:1200px;height:72px;background:var(--red);color:var(--white);text-align:center;font-size:13px;line-height:72px}
</style>
</head>
<body>

<!-- header and hero -->
<div class="abs hero-bg" role="img" aria-label="Dark American flag backdrop behind the header and hero"></div>
<div class="abs soldier-photo" role="img" aria-label="Photo of a soldier in camouflage embracing a child holding a small flag"></div>

<div class="abs brand">
  <div class="brand-mark"></div>
  <div class="brand-name">Anchorwell<br>Giving</div>
</div>

<nav class="abs nav">
  <a style="left:89px">How to Donate</a>
  <a style="left:278px">Why Donate</a>
  <a style="left:441px">FAQ</a>
  <a style="left:534px">About</a>
</nav>

<h1 class="abs hero-title">Donate Boat to Veterans.</h1>

<aside class="abs donate-panel">
  <div class="call">
    <div class="call-icon">
      <svg width="25" height="25" viewBox="0 0 24 24"><path fill="#12287a" d="M6.6 10.8c1.4 2.8 3.8 5.1 6.6 6.6l2.2-2.2c.3-.3.7-.4 1-.2 1.1.4 2.3.6 3.6.6.6 0 1 .4 1 1V20c0 .6-.4 1-1 1C10.6 21 3 13.4 3 4c0-.6.4-1 1-1h3.5c.6 0 1 .4 1 1 0 1.3.2 2.5.6 3.6.1.3 0 .7-.2 1z"/></svg>
    </div>
    <div class="call-label">Call today to donate</div>
    <div class="call-number">1-800-555-0148</div>
  </div>
  <div class="panel-title">Donate your boat online</div>
  <div class="panel-divider"></div>

  <div class="group-label" style="top:195px">Contact Information</div>
  <div class="field" style="left:11px;top:228px;width:175px">First Name</div>
  <div class="field" style="left:192px;top:228px;width:175px">Laste Name</div>
  <div class="field" style="left:11px;top:266px;width:175px">Zip Code</div>
  <div class="field" style="left:192px;top:266px;width:175px">Day Phone</div>
  <div class="field" style="left:11px;top:303px;width:356px">Email Address</div>

  <div class="group-label" style="top:350px">Auto Donation Information</div>
  <div class="field" style="left:11px;top:381px;width:175px">Choose Year<span class="caret"></span></div>
  <div class="field" style="left:192px;top:381px;width:175px">Choose Make<span class="caret"></span></div>
  <div class="field" style="left:11px;top:419px;width:356px">Model of Vehicle</div>

  <div class="submit">Submit Application</div>
</aside>

<!-- benefits -->
<h2 class="abs section-heading" style="top:626px">Donate your boat to&nbsp; veterans!</h2>

<div class="abs benefit" style="left:99px">
  <div class="benefit-icon"><svg width="46" height="46" viewBox="0 0 46 46"><path fill="#fff" d="M8 24c0-8 7-14 15-14h8c4 0 7 3 7 7v4c0 3-3 6-6 6H23l-6 8c-2 3-7 2-8-2z"/></svg></div>
  <div class="benefit-label">You have<br>no costs</div>
</div>
<div class="abs benefit" style="left:293px">
  <div class="benefit-icon"><svg width="50" height="46" viewBox="0 0 50 46"><path fill="#fff" d="M6 26h20v-8h8l6 8v8H6z"/><path stroke="#fff" stroke-width="3" d="M14 26L30 8M30 8v10"/><circle cx="14" cy="35" r="4" fill="#fff" stroke="#12287a" stroke-width="2"/><circle cx="34" cy="35" r="4" fill="#fff" stroke="#12287a" stroke-width="2"/></svg></div>
  <div class="benefit-label">Free towing,<br>running or not</div>
</div>
<div class="abs benefit" style="left:486px">
  <div class="benefit-icon accent"><svg width="44" height="48" viewBox="0 0 44 48"><rect x="6" y="8" width="26" height="34" fill="#7fc9a3" stroke="#1a1a1a" stroke-width="2" transform="rotate(-8 19 25)"/><rect x="12" y="6" width="26" height="34" fill="#a6e0c0" stroke="#1a1a1a" stroke-width="2"/><text x="25" y="28" font-size="14" text-anchor="middle" fill="#1a1a1a" font-family="sans-serif">%</text></svg></div>
  <div class="benefit-label">We issue you an<br>IRS tax receipt</div>
</div>
<div class="abs benefit" style="left:680px">
  <div class="benefit-icon"><svg width="44" height="44" viewBox="0 0 44 44" fill="none" stroke="#fff" stroke-width="2.5"><rect x="6" y="8" width="26" height="30"/><path d="M11 16h16M11 22h16M11 28h10M28 32L40 12"/></svg></div>
  <div class="benefit-label">We take care of<br>all paperwork</div>
</div>
<div class="abs benefit" style="left:874px">
  <div class="benefit-icon"><svg width="40" height="46" viewBox="0 0 40 46" fill="none" stroke="#fff" stroke-width="2.5"><rect x="7" y="7" width="26" height="34" rx="2"/><rect x="14" y="3" width="12" height="7" fill="#fff"/><path d="M13 19h14M13 26h14M13 33h14"/></svg></div>
  <div class="benefit-label">We take care of<br>DMV &amp; Smog issues</div>
</div>

<!-- how to donate -->
<section class="abs how"></section>
<h2 class="abs section-heading" style="top:1030px">How to donate</h2>

<div class="abs step" style="left:142px">
  <div class="step-icon"><svg width="54" height="54" viewBox="0 0 54 54" fill="none" stroke="#fff" stroke-width="3"><circle cx="27" cy="27" r="22"/><path d="M19 15l5 6-3 3c2 4 5 7 9 9l3-3 6 5-3 4c-9 0-20-11-20-20z" fill="#fff" stroke="none"/></svg></div>
  <div class="step-label">Call us at 1-800-555-0148 or<br>fill out the online form</div>
</div>
<div class="abs step" style="left:449px">
  <div class="step-icon"><svg width="60" height="44" viewBox="0 0 60 44"><path fill="#fff" d="M4 26h26V14h10l8 12v8H4z"/><path stroke="#fff" stroke-width="3" d="M8 26L20 6"/><circle cx="14" cy="35" r="5" fill="#fff" stroke="#12287a" stroke-width="2"/><circle cx="42" cy="35" r="5" fill="#fff" stroke="#12287a" stroke-width="2"/></svg></div>
  <div class="step-label">We tow the<br>vehicle</div>
</div>
<div class="abs step" style="left:759px">
  <div class="step-icon"><svg width="50" height="50" viewBox="0 0 50 50" fill="none" stroke="#fff" stroke-width="2.5"><path d="M25 4v10M25 4l-14 14M25 4l14 14"/><rect x="8" y="18" width="34" height="24"/><text x="25" y="35" font-size="12" text-anchor="middle" fill="#fff" stroke="none" font-family="sans-serif" font-weight="700">TAX</text></svg></div>
  <div class="step-label">Tax write-off</div>
</div>

<svg class="abs" style="left:419px;top:1148px" width="62" height="30" viewBox="0 0 62 30" fill="none" stroke="#555" stroke-width="3.5" stroke-linecap="round"><path d="M2 12C20 2 40 2 56 18M56 18l-2-12M56 18l-12 2"/></svg>
<svg class="abs" style="left:748px;top:1148px" width="62" height="30" viewBox="0 0 62 30" fill="none" stroke="#555" stroke-width="3.5" stroke-linecap="round"><path d="M2 14C20 26 40 26 56 12M56 12l-12-2M56 12l-2 12"/></svg>

<!-- faq -->
<h2 class="abs section-heading" style="top:1418px">Frequently asked questions</h2>

<div class="abs faq-item open">
  <div class="faq-q">The standard Lorem Ipsum passage, used since the 1500s</div>
  <span class="faq-toggle" style="top:29px"></span>
  <p class="faq-a">I am text block. Click edit button to change this text. Lorem ipsum dolor sit amet, consectetur adipiscing elit. Ut elit tellus, luctus nec ullamcorper mattis, pulvinar dapibus leo.</p>
</div>
<div class="abs faq-item closed" style="top:1656px">
  <div class="faq-q">Section 1.10.32 of "de Finibus Bonorum et Malorum"</div>
  <span class="faq-toggle plus" style="top:32px"></span>
</div>
<div class="abs faq-item closed" style="top:1748px">
  <div class="faq-q">Section 1.10.33 of "de Finibus Bonorum et Malorum", written</div>
  <span class="faq-toggle plus" style="top:32px"></span>
</div>

<div class="abs parade-photo" role="img" aria-label="Photo of uniformed veterans marching in a parade carrying American flags"></div>

<!-- footer -->
<svg class="abs footer-tab" viewBox="0 0 228 78"><path d="M16 0H212L228 78H0z" fill="#12287a"/></svg>
<div class="abs footer-tab-brand">
  <div class="dot"></div>
  <span>Anchorwell<br>Giving</span>
</div>

<footer class="abs footer" role="img" aria-label="Dark flag and uniform backdrop behind the footer"></footer>

<h3 class="abs footer-heading" style="left:90px">About us</h3>
<p class="abs footer-about">But I must explain to you how all this mistaken idea of denouncing pleasure and praising pain was born and I will give you a complete account of the system, and expound the actual teachings of the great explorer of the truth,..</p>

<h3 class="abs footer-heading" style="left:495px">Sitemap</h3>
<ul class="abs sitemap">
  <li>How to donate</li>
  <li>Why donate</li>
  <li>FAQ</li>
  <li>About</li>
</ul>

<h3 class="abs footer-heading" style="left:791px">Stay in touch</h3>
<div class="abs newsletter-input">Enter your email</div>
<div class="abs newsletter-btn">SIGN UP</div>
<span class="abs social" style="left:793px;background:#3b5a9a"></span>
<span class="abs social" style="left:822px;background:#3ea7e0"></span>
<span class="abs social" style="left:851px;background:#d9453a"></span>
<span class="abs social" style="left:880px;background:#e02a20"></span>
<span class="abs social" style="left:909px;background:#c13584"></span>

<div class="abs copyright">Copyright (c) 2017. Anchorwell Giving. All rights reserved.</div>

</body>
</html>
```